Bussiness Card- KU Architects

We are seeking a new business for our practice. We produce innovative architecture for our clients in the field of education, community servise, residential and the retail sector.
We would like to use our new logo attached. Borrow from old card where suitable eg the back section.
Our old card is attached.

Our Updated Contact Details are:
KU Architects. ABN 57 614 302 948
T: 07 3498 2260 F:07 3815 4027 M: 0452 718 904
47 Marrow Street, Fernhill Park, Queensland 4102
kuarchitects@fernmail.com.au
www.kuarchitects.net.au

Our new logo is attached
The final design should communicate an innovative practice, professional service and a commitment to quality

Target Market(s)

Education Client
Corporate Clients
Community Organisations

Industry/Entity Type

Professional Service

```html
<!DOCTYPE html>
<html lang="en">
<head>
<meta charset="utf-8">
<title>KU Architects – Business Card</title>
<link href="https://fonts.googleapis.com/css2?family=Arimo:wght@400&family=Cinzel:wght@400&display=swap" rel="stylesheet">
<style>
  :root{
    --bg:#d9d9d9;
    --paper:#f4f4f4;
    --green:#8cc751;
    --green-deep:#7dbb42;
    --green-light:#9ed36a;
    --stripe:#c9c9c9;
    --ink:#4a4a4a;
    --ink-soft:#7a7a7a;
  }
  *{margin:0;padding:0;box-sizing:border-box}
  html,body{width:1200px;height:864px;overflow:hidden}
  body{background:var(--bg);font-family:"Arimo",Arial,sans-serif;position:relative}

  .card{position:absolute;width:540px;height:310px;background:var(--paper);
        box-shadow:0 6px 18px rgba(0,0,0,.22);overflow:hidden}
  .card--front{left:50px;top:480px}
  .card--back{left:610px;top:80px}

  .wordmark{display:flex;align-items:center;gap:10px}
  .wordmark__dot{width:22px;height:22px;border-radius:50%;background:var(--green);flex:none}
  .wordmark__name{font-family:"Arimo",Arial,sans-serif;font-weight:400;font-size:30px;
        color:var(--green);line-height:1}
  .tagline{font-family:"Arimo",Arial,sans-serif;font-size:12px;
        letter-spacing:2px;color:var(--ink-soft)}

  /* front */
  .front__head{position:absolute;left:0;top:0;width:100%;height:118px}
  .front__brand{position:absolute;left:28px;top:22px}
  .front__brand .tagline{margin:8px 0 0 32px}
  .abn{position:absolute;left:28px;top:94px;font-size:13px;color:var(--ink)}
  .person{position:absolute;right:26px;top:72px}
  .person__name{font-family:"Cinzel",serif;font-size:17px;letter-spacing:1px;color:var(--ink)}
  .person__quals{font-size:10.5px;color:var(--ink);margin-top:1px}
  .front__stripe{position:absolute;left:0;top:118px;width:100%;height:5px;background:var(--stripe)}
  .front__band{position:absolute;left:0;top:123px;width:100%;height:187px;
        background:linear-gradient(160deg,var(--green-light) 0%,var(--green) 45%,var(--green-deep) 100%)}
  .contacts{list-style:none;position:absolute;left:22px;top:16px}
  .contacts li{display:flex;align-items:center;height:24px;font-size:14.5px;color:var(--ink)}
  .contacts svg{width:14px;height:14px;margin-right:16px;flex:none}

  /* back */
  .back__brand{position:absolute;left:36px;top:118px}
  .back__brand .tagline{margin:8px 0 0 32px}
  .back__rule{position:absolute;left:350px;top:40px;width:2px;height:230px;background:var(--green)}
  .sectors{list-style:none;position:absolute;left:390px;top:50px}
  .sectors li{font-size:15px;color:var(--green);height:44px;line-height:24px}
</style>
</head>
<body>

<section class="card card--front" aria-label="Business card front">
  <div class="front__head">
    <div class="front__brand">
      <div class="wordmark">
        <span class="wordmark__dot"></span>
        <span class="wordmark__name">KU Architects</span>
      </div>
      <div class="tagline">Designing Places Together</div>
    </div>
    <div class="abn">ABN 57 614 302 948</div>
    <div class="person">
      <div class="person__name">Marco Delacourt</div>
      <div class="person__quals">M Arch(qut) B Design(qut)</div>
    </div>
  </div>
  <div class="front__stripe"></div>
  <div class="front__band">
    <ul class="contacts">
      <li>
        <svg viewBox="0 0 16 16" fill="#fff"><path d="M4 1l2.5 3-1.5 1.5c.8 2 2.5 3.7 4.5 4.5L11 8.5l3 2.5-1.5 3C7 13.5 2.5 9 2 3.5z"/></svg>
        <span>07 3498 2260</span>
      </li>
      <li>
        <svg viewBox="0 0 16 16" fill="none" stroke="#fff" stroke-width="1.5"><rect x="4" y="1.5" width="8" height="13" rx="1.5"/></svg>
        <span>0452 718 904</span>
      </li>
      <li>
        <svg viewBox="0 0 16 16" fill="#fff"><rect x="4" y="1" width="8" height="5"/><rect x="1" y="6" width="14" height="6" rx="1"/><rect x="4" y="10" width="8" height="5"/></svg>
        <span>07 3815 4027</span>
      </li>
      <li>
        <svg viewBox="0 0 16 16" fill="#fff"><path d="M8 1a5 5 0 0 1 5 5c0 3.5-5 9-5 9S3 9.5 3 6a5 5 0 0 1 5-5z"/></svg>
        <span>47 Marrow Street, Fernhill Park, Queensland 4102</span>
      </li>
      <li>
        <svg viewBox="0 0 16 16" fill="none" stroke="#fff" stroke-width="1.5"><rect x="1.5" y="3.5" width="13" height="9"/><path d="M1.5 3.5L8 9l6.5-5.5"/></svg>
        <span>kuarchitects@fernmail.com.au</span>
      </li>
      <li>
        <svg viewBox="0 0 16 16" fill="none" stroke="#fff" stroke-width="1.4"><circle cx="8" cy="8" r="6.5"/><ellipse cx="8" cy="8" rx="3" ry="6.5"/><path d="M1.5 8h13"/></svg>
        <span>www.kuarchitects.net.au</span>
      </li>
    </ul>
  </div>
</section>

<section class="card card--back" aria-label="Business card back">
  <div class="back__brand">
    <div class="wordmark">
      <span class="wordmark__dot"></span>
      <span class="wordmark__name">KU Architects</span>
    </div>
    <div class="tagline">Designing Places Together</div>
  </div>
  <div class="back__rule"></div>
  <ul class="sectors">
    <li>Education</li>
    <li>Residential</li>
    <li>Commercial</li>
    <li>Retail</li>
    <li>Interiors</li>
  </ul>
</section>

</body>
</html>
```